Letterhead design for Sleep Consulting Business

I'm looking for a new letterhead (heading/footer) design for my Sleep Consulting Business, I work with families to help their children improve their sleep.

The heading/footer will used in Microsoft Word Only-to be used for all of my documents such as writing Sleep Plans. I need to utilize as much working space in the document as possible. This will NOT be printed out on paper- it will only be used for heading/footer on microsoft word, then emailed to clients, who may print it at home.

My brand colors:
Dark Blue Hex: 1F2A42
Lighter Blueish Hex: 90BEC9
You're welcome to check out my website for inspiration- it is freshly created with other colors as well, and I love the outcome. www.hollowpinerest.com

Target Market(s)

Tired parents

Font styles to use
Script
Other font styles liked:
• Great Vibe, Lato or Just Another Hand are all used currently for my brand. Open to other options.

Requirements
Must have
• The letterhead (heading/footer) MUST be kept narrow (height-wise), so I have plenty of space on my document, while including important information.

It should look professional on screen, and when printed.

Must include my business name OR logo (Hollow Pine Sleep Consulting), and my email address. Mara@hollowpinerest.com

Website is optional, not required, just if you need to fill in a spot: www.hollowpinerest.com

```html
<!DOCTYPE html>
<html lang="en">
<head>
<meta charset="utf-8">
<title>Hollow Pine Sleep Consulting – Letterhead</title>
<link rel="stylesheet" href="https://fonts.googleapis.com/css2?family=Great+Vibes&family=Lato:wght@400;700&display=swap">
<style>
  :root {
    --navy: #1F2A42;
    --sky: #90BEC9;
    --paper: #eeedee;
    --ink: #2b2b30;
    --muted: #6d6d72;
    --accent-red: #b0151c;
    --backdrop: #8ea6a8;
  }
  * { box-sizing: border-box; margin: 0; padding: 0; }
  html, body {
    width: 1192px; height: 1200px; overflow: hidden;
    background: var(--backdrop);
  }
  .sheet {
    position: absolute; left: 186px; top: 20px;
    width: 820px; height: 1160px;
    background: var(--paper);
    overflow: hidden;
    font-family: "Lato", sans-serif;
    color: var(--ink);
  }
  .sheet-bands { position: absolute; inset: 0; width: 820px; height: 1160px; }

  .brand {
    position: absolute; left: 17px; top: 101px;
    display: flex; align-items: center; gap: 12px;
  }
  .brand-dot {
    width: 56px; height: 56px; border-radius: 50%;
    background: var(--sky);
  }
  .brand-name {
    font-family: "Lato", sans-serif; font-weight: 400;
    font-size: 22px; color: var(--navy); letter-spacing: 0.2px;
  }

  .contact { position: absolute; left: 580px; top: 82px; color: var(--navy); }
  .contact-title {
    font-family: "Great Vibes", cursive; font-size: 19px; line-height: 24px;
    white-space: nowrap;
  }
  .contact-list { list-style: none; margin: 4px 0 0 16px; font-size: 10.5px; line-height: 16.5px; }
  .contact-list li { display: flex; align-items: center; gap: 4px; white-space: nowrap; }
  .contact-list svg { width: 9px; height: 9px; flex: none; }

  .letter { position: absolute; left: 62px; top: 202px; width: 630px; }
  .recipient-label { font-size: 17px; line-height: 22px; margin-bottom: 14px; }
  .recipient-name { font-size: 18px; line-height: 19px; color: var(--accent-red); letter-spacing: 0.4px; }
  .recipient-role { font-size: 12px; line-height: 12px; color: var(--muted); }
  .recipient-details { font-size: 17.5px; line-height: 19.5px; letter-spacing: 0.3px; margin-bottom: 18px; }
  .letter-body p { font-size: 16.6px; line-height: 19.2px; margin-bottom: 19px; }
  .letter-body p.section-break { margin-top: 19px; }
</style>
</head>
<body>
<main class="sheet">
  <svg class="sheet-bands" viewBox="0 0 820 1160" aria-hidden="true">
    <path fill="var(--navy)" d="M0 0 H820 V172 C805 102 760 42 690 40 C560 38 420 80 300 88 C200 95 80 70 0 44 Z"/>
    <path fill="none" stroke="var(--sky)" stroke-width="7" d="M0 54 C80 80 200 104 300 97 C420 88 560 50 690 50 C752 52 796 100 814 162"/>
    <path fill="var(--navy)" d="M0 940 C14 1010 70 1046 180 1052 C280 1058 360 1052 402 1040 C330 1064 220 1077 120 1073 C60 1071 20 1062 0 1052 Z"/>
    <path fill="none" stroke="var(--sky)" stroke-width="7" d="M8 1068 C100 1094 250 1094 420 1075 C560 1058 700 1048 820 1104"/>
    <path fill="var(--navy)" d="M0 1088 C100 1110 250 1108 420 1090 C560 1074 700 1066 820 1120 V1160 H0 Z"/>
  </svg>

  <div class="brand">
    <span class="brand-dot"></span>
    <span class="brand-name">Hollow Pine Sleep Consulting</span>
  </div>

  <div class="contact">
    <p class="contact-title">Hollow Pine Sleep Consulting</p>
    <ul class="contact-list">
      <li><svg viewBox="0 0 10 10"><path fill="var(--navy)" d="M2 0.5 L3.6 2.6 L2.7 3.6 C3.3 5 4.9 6.6 6.4 7.3 L7.4 6.4 L9.5 8 L8.4 9.5 C4.5 9.2 0.8 5.5 0.5 1.6 Z"/></svg>555-201-7388</li>
      <li><svg viewBox="0 0 10 10"><rect x="0.6" y="2" width="8.8" height="6" fill="none" stroke="var(--navy)" stroke-width="0.9"/><path d="M0.6 2 L5 5.4 L9.4 2" fill="none" stroke="var(--navy)" stroke-width="0.9"/></svg>mara@hollowpinerest.com</li>
      <li><svg viewBox="0 0 10 10"><circle cx="5" cy="5" r="4.3" fill="none" stroke="var(--navy)" stroke-width="0.9"/><path d="M0.7 5 H9.3 M5 0.7 C3 3 3 7 5 9.3 M5 0.7 C7 3 7 7 5 9.3" fill="none" stroke="var(--navy)" stroke-width="0.8"/></svg>www.hollowpinerest.com</li>
    </ul>
  </div>

  <article class="letter">
    <p class="recipient-label">TO</p>
    <p class="recipient-name">HARLOW</p>
    <p class="recipient-role">Director</p>
    <p class="recipient-details">Design Studio<br>A: 555 310 482<br>B: 555 0192 736</p>
    <div class="letter-body">
      <p>Lorem ipsum dolor sit amet, consectetur adipiscing elit. Vestibulum consectetur egestas metus, quis scelerisque tortor consectetur sed. Nullam sit amet lorem sed arcu faucibus semper. Vestibulum ante ipsum primis in faucibus orci luctus et ultrices posuere cubilia Curae; Sed sagittis arcu ut ligula molestie malesuada. Suspendisse posuere tincidunt elit, at ullamcorper augue blandit vitae.</p>
      <p>Cras egestas vestibulum pulvinar. Donec iaculis imperdiet hendrerit. Sed mollis, enim quis hendrerit dictum, tortor mauris vulputate ligula, viverra porta magna libero at mi. Integer odio nisl, luctus nec dui in, rutrum sollicitudin nisi. Suspendisse nec erat eros.</p>
      <p>Sed dictum quam arcu, sit amet ullamcorper orci faucibus eget. Morbi finibus ante at risus commodo, nec ullamcorper nulla tincidunt. Integer eu molestie nulla, sed consequat tortor. Sed ullamcorper congue metus, vitae dictum nibh luctus sed. Suspendisse ornare purus fermentum, viverra elit sed, bibendum ex. Vivamus semper diam vel diam laoreet rutrum. Ut porta fermentum velit. Vestibulum vitae semper nisl. Sed facilisis at ex et vestibulum. Donec at magna ut eros pulvinar hendrerit.</p>
      <p class="section-break">Sed dictum quam arcu, sit amet ullamcorper orci faucibus eget. Morbi finibus ante at risus commodo, nec ullamcorper nulla tincidunt. Integer eu molestie nulla, sed consequat tortor. Sed ullamcorper congue metus, vitae dictum nibh luctus sed. Suspendisse ornare purus fermentum, viverra elit sed, bibendum ex.</p>
      <p>Vivamus semper diam vel diam laoreet rutrum. Ut porta fermentum velit. Vestibulum vitae semper nisl. Sed facilisis at ex et vestibulum. Donec at magna ut eros pulvinar hendrerit.</p>
    </div>
  </article>
</main>
</body>
</html>
```